Klassisches Visitenkarten-Design mit braunen Farbtönen gesucht
Zielgruppe
Meine Firma bietet Pferdezahnbehandlungen, Pferdefütterungsberatung sowie Trensen- und Gebissanpassungen an. Ausserdem habe ich eine mobile Pferdewaage. Meine Kunden sind Pferdebesitzer der gehobenen Klasse, die gerne Geld in die Hand nehmen um ihr Tier korrekt zu halten/versorgen.
Ich setze bisher auf ein klassisches Design in braun Tönen.
Aufgabenstellung
Mir ist eine klare, schnörkellose Botschaft wichtig.
Ich möchte mich gerne mit klassischem, aber auch sehr schönem Design von der Konkurrenz abheben.
Der Fokus soll auf der wissenschaftlichen Arbeitsweise mit dem Partner Pferd liegen.
Im Anhang sind Fotos von der alten Visitenkarten. Dort fehlt mir aber die klare Linie.
Normalerweise arbeite ich mit der Schriftart Eurostyle, bin aber auch für neue Vorschläge offen.

```html
<!DOCTYPE html>
<html lang="de">
<head>
<meta charset="utf-8">
<title>EQUAVIA – Visitenkarte</title>
<link href="https://fonts.googleapis.com/css2?family=Michroma&family=Jura:wght@400;500&display=swap" rel="stylesheet">
<style>
  :root {
    --bg: #f4f3f1;
    --brown-deep: #5e2410;
    --brown-text: #6a2c12;
    --brown-soft: #a9765f;
    --paper: #ffffff;
    --light: #ffffff;
  }
  * { margin: 0; padding: 0; box-sizing: border-box; }
  html, body { width: 1200px; height: 873px; overflow: hidden; background: var(--bg); }
  .canvas {
    position: relative; width: 1200px; height: 873px;
    display: flex; justify-content: center; align-items: center; gap: 90px;
  }
  .card {
    width: 340px; height: 530px; position: relative;
    box-shadow: 0 6px 20px rgba(0,0,0,0.12);
  }
  .card--front { background: var(--brown-deep); color: var(--light); }
  .card--back { background: var(--paper); color: var(--brown-text); }

  .emblem-field {
    position: absolute; left: 85px; top: 70px; width: 170px; height: 170px;
    border-radius: 50%; background: var(--brown-soft); opacity: 0.55;
  }
  .front-text {
    position: absolute; right: 34px; bottom: 48px; text-align: left;
    font-family: "Jura", sans-serif;
  }
  .brand-name {
    font-family: "Michroma", sans-serif; font-size: 36px; letter-spacing: 2px;
    line-height: 1; margin-bottom: 12px;
  }
  .service { font-size: 15px; letter-spacing: 0.6px; line-height: 1.45; text-transform: uppercase; }
  .service--small { font-size: 12.5px; }
  .service--large { font-size: 17px; }

  .back-mark {
    display: flex; align-items: center; justify-content: center; gap: 10px;
    margin: 70px auto 0; width: max-content;
  }
  .back-mark .dot { width: 18px; height: 18px; border-radius: 50%; background: var(--brown-text); }
  .back-mark .wordmark { font-family: "Michroma", sans-serif; font-size: 18px; letter-spacing: 2px; color: var(--brown-text); }
  .contact {
    text-align: center; font-family: "Jura", sans-serif; font-size: 16px; line-height: 1.35;
    margin-top: 70px;
  }
  .person-name { font-family: "Michroma", sans-serif; font-size: 17px; letter-spacing: 0.5px; }
  .person-title { font-size: 15.5px; margin-bottom: 28px; }
  .address { margin-bottom: 24px; }
</style>
</head>
<body>
<main class="canvas">
  <section class="card card--front">
    <div class="emblem-field" role="img" aria-label="Fläche für das Pferdekopf-Emblem"></div>
    <div class="front-text">
      <p class="brand-name">EQUAVIA</p>
      <p class="service">Pferdezahnbehandlung</p>
      <p class="service service--small">Pferdefütterungsberatung</p>
      <p class="service service--large">Mobile Pferdewaage</p>
    </div>
  </section>

  <section class="card card--back">
    <div class="back-mark">
      <span class="dot"></span>
      <span class="wordmark">EQUAVIA</span>
    </div>
    <div class="contact">
      <p class="person-name">MARLENE T. HAUSNER</p>
      <p class="person-title">Agrarwissenschaften (Dr. sc.)</p>
      <p class="address">Lindenweg 14<br>79801 Tannau/ Hochschwarzwald</p>
      <p>0171 5538209<br>kontakt@equa-zahnpflege.com<br>www.equavia-pferd.de</p>
    </div>
  </section>
</main>
</body>
</html>
```